Velmont Hamper company needs a brochure design

We need a brochure design for a new company in Dubai called 'Velmont Hampers'. We already have a logo designed which I have attached and would like to use this and the green/gold/white colours for our brochure. Our company initially will be supplying Velmont Hamper wear of traditional wicker baskets in many designs which hold all the cutlery, crockery and accessories. We will also be selling picnic accessories. We want to purvey a sense of luxury and class in line with our logo. I have attached some photos of the picnicwear. As our products are changing all the time I thought a fold out cover which stays the same and then product cards inserted into the folder which can be changed according to our product changes. I am looking for a fairly simple design and each product card should have at least one photo of the product on it with a spec and description also. On the cover of the folder I would like room to write about the company and what we do, this can be inside or out and may or may not include photos. I have the logo designs in illustrator format and pdf. Please contact if any more information is needed.

Reason: I have extended this deadline as there are some content changes taking place.

```html
<!DOCTYPE html>
<html lang="en">
<head>
<meta charset="utf-8">
<title>Velmont Hampers – Product Cards</title>
<link href="https://fonts.googleapis.com/css2?family=Cinzel:wght@500;700&family=Lato:wght@400;700;900&display=swap" rel="stylesheet">
<style>
  :root{
    --green:#1e4a1c;
    --green-deep:#163a15;
    --gold:#d9b227;
    --gold-soft:#e7c55a;
    --white:#ffffff;
    --page:#ececea;
    --ink:#2a2a2a;
    --wicker-a:#c99a55;
    --wicker-b:#8a5f2c;
  }
  *{box-sizing:border-box;margin:0;padding:0}
  html,body{width:1200px;height:923px;overflow:hidden;background:var(--page)}
  body{position:relative;font-family:"Lato",sans-serif}

  .card{position:absolute;background:var(--white);overflow:hidden;box-shadow:0 6px 18px rgba(0,0,0,.18)}
  .card svg.shapes{position:absolute;inset:0;width:100%;height:100%}
  .photo{position:absolute;background:linear-gradient(160deg,#eee6d3 0%,var(--wicker-a) 55%,var(--wicker-b) 100%);border-radius:4px}

  /* product card */
  .product{left:40px;top:136px;width:420px;height:651px}
  .brand{position:absolute;left:0;right:0;top:38px;text-align:center}
  .brand-mark{width:14px;height:14px;border-radius:50%;background:var(--gold);margin:0 auto 10px}
  .brand-name{font-family:"Cinzel",serif;font-weight:500;color:var(--gold);font-size:19px;letter-spacing:3px}
  .product .photo{left:70px;top:190px;width:280px;height:225px}
  .product-title{position:absolute;left:0;right:0;top:462px;text-align:center;font-weight:900;font-size:34px;color:var(--gold);letter-spacing:.5px}
  .product-desc{position:absolute;left:18px;right:18px;top:510px;text-align:center;color:var(--white);font-size:12.6px;line-height:1.42}

  /* overview card */
  .overview{left:490px;top:136px;width:420px;height:651px}
  .overview-title{position:absolute;left:22px;top:42px;font-weight:900;font-size:27px;color:var(--gold)}
  .spec-list{position:absolute;top:150px;list-style:none;font-size:11.6px;color:var(--ink);line-height:1.25}
  .spec-list li{position:relative;padding-left:16px;margin-bottom:6px}
  .spec-list li::before{content:"";position:absolute;left:0;top:3px;width:8px;height:8px;border-radius:50%;background:var(--gold)}
  .spec-left{left:22px;width:190px}
  .spec-right{left:222px;width:180px}
  .overview .photo{left:60px;top:370px;width:300px;height:200px}

  /* business card */
  .contact-card{left:940px;top:600px;width:220px;height:135px}
  .mini-brand{position:absolute;right:10px;top:12px;font-family:"Cinzel",serif;font-weight:500;color:var(--gold);font-size:9px;letter-spacing:1px}
  .contact-card .photo{left:10px;top:38px;width:86px;height:66px}
  .mini-title{position:absolute;left:104px;top:38px;font-weight:900;font-size:12px;color:var(--green)}
  .mini-text{position:absolute;left:104px;top:54px;width:108px;font-size:5.6px;line-height:1.35;color:var(--ink)}
  .contact-line{position:absolute;right:8px;display:flex;align-items:center;gap:4px;color:var(--white);font-size:7px;font-weight:700}
  .contact-line svg{width:8px;height:8px}
  .phone{top:110px}
  .web{top:121px}
</style>
</head>
<body>

<article class="card product">
  <svg class="shapes" viewBox="0 0 420 651" preserveAspectRatio="none" aria-hidden="true">
    <path d="M0 0H420V142Q250 132 0 176Z" fill="var(--green)"/>
    <path d="M0 176Q250 132 420 142V152Q250 146 0 188Z" fill="var(--gold)"/>
    <path d="M0 452Q210 420 420 430V440Q210 432 0 466Z" fill="var(--gold)"/>
    <path d="M0 466Q210 432 420 440V651H0Z" fill="var(--green)"/>
  </svg>
  <div class="brand">
    <div class="brand-mark"></div>
    <div class="brand-name">VELMONT HAMPERS</div>
  </div>
  <div class="photo" role="img" aria-label="Photo of an open wicker picnic hamper fitted with plates, cutlery, flask and mugs"></div>
  <h1 class="product-title">THE ASHCOMBE</h1>
  <p class="product-desc">This luxury fitted picnic basket is the epitome of stylish outdoor dining, hand crafted in honey coloured buff willow with tan leather straps and trims it comes equipped for four people. Internally the basket is furnished with beautiful cream fabrics including stylish napkins, a stainless steel flask and ceramic mugs are included to ensure that a perfect cup of tea can be enjoyed outside. Wine glasses are also included to ensure that this is the perfect accessory for a leisurely afternoon tea with family or friends.</p>
</article>

<article class="card overview">
  <svg class="shapes" viewBox="0 0 420 651" preserveAspectRatio="none" aria-hidden="true">
    <path d="M0 0H420V120Q200 70 0 98Z" fill="var(--green)"/>
    <path d="M0 98Q200 70 420 120V130Q200 82 0 108Z" fill="var(--gold)"/>
    <path d="M0 651V600Q30 620 80 651Z" fill="var(--gold)"/>
    <path d="M120 651Q300 560 420 540V651Z" fill="var(--green)"/>
    <path d="M110 651Q290 548 420 528V540Q300 560 126 651Z" fill="var(--gold)"/>
  </svg>
  <h2 class="overview-title">Picnic basket overview:</h2>
  <ul class="spec-list spec-left">
    <li>Handmade light buff willow for four people</li>
    <li>Tan leather straps and trim</li>
    <li>Removable cream cooler bag</li>
    <li>Contemporary cream and white colour palette</li>
    <li>4 white china plates</li>
    <li>4 stainless steel knives, forks and spoons</li>
    <li>1 Stainless steel waiters friend bottle opener</li>
  </ul>
  <ul class="spec-list spec-right">
    <li>Stainless steel salt and pepper mills</li>
    <li>1 Stainless steel flask</li>
    <li>4 Cream napkins</li>
    <li>1 wooden chopping board</li>
    <li>4 wine glasses</li>
    <li>4 China mugs held in a willow basket, 240 x 140 x 110mm</li>
    <li>Hamper dimensions 380 x 300 x 210mm</li>
  </ul>
  <div class="photo" role="img" aria-label="Photo of a closed wicker picnic hamper with handle and side lids open"></div>
</article>

<aside class="card contact-card">
  <svg class="shapes" viewBox="0 0 220 135" preserveAspectRatio="none" aria-hidden="true">
    <path d="M70 0H220V30Q150 24 70 0Z" fill="var(--green)"/>
    <path d="M70 0Q150 24 220 30V33Q150 28 70 0Z" fill="var(--gold)"/>
    <path d="M0 112Q110 100 220 104V135H0Z" fill="var(--green)"/>
    <path d="M0 108Q110 96 220 100V104Q110 100 0 112Z" fill="var(--gold)"/>
  </svg>
  <div class="mini-brand">VELMONT HAMPERS</div>
  <div class="photo" role="img" aria-label="Photo of an open fitted wicker picnic hamper"></div>
  <div class="mini-title">THE ASHCOMBE</div>
  <p class="mini-text">A fitted willow hamper for four, with cream fabrics, china plates, steel cutlery, flask and glasses for a relaxed afternoon outdoors.</p>
  <div class="contact-line phone">
    <svg viewBox="0 0 10 10" aria-hidden="true"><path d="M2 1l2 2-1 1.2a6 6 0 0 0 2.8 2.8L7 6l2 2-1.2 1.2C4.5 9 1 5.5.8 2.2Z" fill="var(--gold)"/></svg>
    000 000 000
  </div>
  <div class="contact-line web">
    <svg viewBox="0 0 10 10" aria-hidden="true"><circle cx="5" cy="5" r="4" fill="none" stroke="var(--gold)" stroke-width="1.2"/></svg>
    velmonthampers.ae
  </div>
</aside>

</body>
</html>
```